Velduna.com webside

I want to build a Velduna.com retail website use on Shopify, reselling three main categories: Office Supplies, Packing Supplies, and Home Consumables. I also wish the webpage has the same functions as the Corvelt home page. The page is split into three different parts with the top being a sliding screen showcasing promotion products, below it being the three categories, and finally, a moving screen showing company missions.
Target Market(s)
U.S online
Industry/Entity Type
Office Supplies, packing Supplies and Home Consumables
Coding
Coded - Design and coding required
Number of Pages Required
5+ page
Look and feel

```html
<!DOCTYPE html>
<html lang="en">
<head>
<meta charset="utf-8">
<title>Velduna.com – Office, Packing &amp; Home Supplies</title>
<link href="https://fonts.googleapis.com/css2?family=Roboto:ital,wght@0,400;0,500;0,700;1,400&display=swap" rel="stylesheet">
<style>
:root{
  --green:#17a689;
  --green-dark:#0f8c73;
  --mint:#c8ede4;
  --ink:#1e1e1e;
  --muted:#555;
  --line:#e2e2e2;
  --page:#f4f5f5;
  --white:#fff;
  --footer:#eeeeee;
}
*{box-sizing:border-box;margin:0;padding:0}
html,body{width:1200px;height:5245px;overflow:hidden}
body{font-family:"Roboto",Arial,sans-serif;color:var(--ink);background:var(--page);position:relative}
a{color:inherit;text-decoration:none}
.abs{position:absolute}
.ph{display:block}

/* header */
.topbar{position:absolute;left:0;top:0;width:1200px;height:84px;background:var(--green);color:#fff}
.logo{font-weight:700;font-size:30px;letter-spacing:-.3px}
.topbar .logo{position:absolute;left:92px;top:20px}
.search{position:absolute;left:288px;top:20px;width:504px;height:44px;background:#fff;border-radius:22px;display:flex;align-items:center;font-size:11px;color:#666}
.search .cat{width:76px;padding-left:20px;border-right:1px solid #ddd;height:26px;display:flex;align-items:center;gap:18px;color:#333}
.search .kw{padding-left:14px;flex:1}
.search svg{margin-right:18px}
.acct{position:absolute;top:20px;font-size:12px;line-height:18px}
.acct b{display:block;font-size:15px;font-weight:700}
.navbar{position:absolute;left:0;top:84px;width:1200px;height:73px;background:#fff;border-bottom:1px solid var(--line)}
.navbar ul{list-style:none;position:absolute;top:31px;left:0;font-size:11.5px;font-weight:500}
.navbar li{position:absolute;white-space:nowrap}
.navbar .cart{position:absolute;top:30px;left:1000px;display:flex;gap:12px;align-items:center;font-size:10.5px}

/* hero */
.hero{position:absolute;left:0;top:157px;width:1200px;height:551px;background:linear-gradient(120deg,#d8f3ec 0%,#b9e7dc 55%,#cdeee6 100%);overflow:hidden}
.hero h1{position:absolute;left:96px;top:114px;font-size:41px;line-height:51px;font-weight:700;width:520px}
.hero .sale{position:absolute;left:96px;top:275px;width:258px;height:38px;border-top:2px solid #222;border-bottom:2px solid #222;font-size:23px;font-weight:500;line-height:34px;padding-left:14px}
.btn{display:inline-block;background:var(--green);color:#fff;font-weight:700;border-radius:20px;text-align:center}
.hero .btn{position:absolute;left:96px;top:340px;width:132px;height:32px;line-height:32px;font-size:14px;border:2px solid #fff}
.hero .art{position:absolute;left:592px;top:47px;width:541px;height:469px;background:linear-gradient(180deg,#a9d9ce 0%,#6f8f88 55%,#2d2d2d 100%);border-radius:6px;opacity:.85}

.notice{position:absolute;left:0;top:708px;width:1200px;height:52px;background:#fff;font-size:13px;text-align:center;line-height:50px;color:#333}
.notice a{color:var(--green);text-decoration:underline}

/* categories */
.catcard{position:absolute;top:760px;width:244px;height:403px;background:#fff;text-align:center}
.catcard h3{font-size:16px;font-weight:500;margin-top:22px}
.catcard .grid{position:absolute;left:18px;top:58px;width:208px;display:grid;grid-template-columns:1fr 1fr;row-gap:36px;column-gap:20px}
.catcard .item .ph{height:82px;border-radius:4px}
.catcard .item .label{display:block;font-size:12.5px;line-height:15px;margin-top:12px;white-space:nowrap}
.outline-btn{display:inline-block;border:2px solid var(--green);color:var(--green);font-size:9.5px;font-weight:700;border-radius:14px;text-align:center}
.catcard .outline-btn{position:absolute;left:75px;top:350px;width:94px;height:26px;line-height:22px}
.signin{position:absolute;left:871px;top:760px;width:245px;height:148px;background:#fff;padding:22px 30px}
.signin h3{font-size:20px;line-height:25px;font-weight:700}
.signin .outline-btn{margin-top:12px;width:150px;height:34px;line-height:30px;font-size:10px;border-radius:18px}
.ship{position:absolute;left:871px;top:928px;width:245px;height:235px;background:var(--green);color:#fff;text-align:center;font-weight:700;font-size:16px;line-height:22px;padding-top:20px}
.ship .ph{position:absolute;left:0;top:80px;width:245px;height:155px;background:linear-gradient(180deg,#17a689 0%,#c79a66 45%,#b0844f 100%)}

/* product panels */
.panel{position:absolute;left:96px;width:1018px;background:#fff}
.panel h2{position:absolute;left:16px;font-size:28px;font-weight:700;white-space:nowrap}
.panel h2 a{font-size:17px;color:var(--green);text-decoration:underline;font-weight:700;margin-left:30px;vertical-align:middle}
.card{position:absolute;width:234px;border:2px solid var(--line);background:#fff;text-align:center}
.card .ph{margin:24px auto 0;width:190px;height:176px;border-radius:4px}
.card .name{font-size:17px;margin-top:22px}
.card .price{font-size:16px;color:var(--green);font-weight:700;margin-top:8px}
.card .outline-btn{margin-top:14px;width:96px;height:28px;line-height:24px}
.arrow{position:absolute;width:36px;height:62px;background:var(--green);display:flex;align-items:center;justify-content:center}
.arrow.l{border-radius:0 31px 31px 0}
.arrow.r{border-radius:31px 0 0 31px}

/* features */
.feature{position:absolute;top:2218px;width:326px;height:445px;background:#fff;border:2px solid var(--line)}
.feature h2{position:absolute;left:18px;top:28px;font-size:28px;font-weight:700}
.feature .ph{position:absolute;left:18px;top:80px;width:288px;height:282px}
.feature a{position:absolute;left:18px;top:386px;font-size:17px;font-weight:700;color:var(--green)}

/* mission */
.mission h2{position:absolute;left:96px;top:3898px;font-size:35px;font-weight:700}
.mission p{position:absolute;left:96px;top:3972px;width:398px;font-size:12.2px;line-height:21.6px;color:#333}
.mission .btn{position:absolute;left:96px;top:4212px;width:152px;height:36px;line-height:36px;font-size:15px;border-radius:18px}
.mission .ph{position:absolute;border:3px solid #fff}

/* testimonials */
.testi{position:absolute;left:0;top:4346px;width:1200px;height:480px;background:linear-gradient(180deg,#13a085 0%,#1aa98c 50%,#129a80 100%);color:#fff;text-align:center}
.testi h2{position:absolute;left:0;width:1200px;top:86px;font-size:38px;font-weight:700}
.testi .quote{position:absolute;left:0;width:1200px;top:136px;font-size:80px;font-weight:700;line-height:80px}
.testi p{position:absolute;left:230px;width:740px;top:232px;font-style:italic;font-size:17.5px;line-height:24px}
.testi .avatar{position:absolute;left:490px;top:331px;width:90px;height:90px;border-radius:50%;background:#c89a80;border:3px solid #fff}
.testi .who{position:absolute;left:594px;top:360px;text-align:left;font-size:19px;font-weight:700}
.testi .stars{display:flex;gap:3px;margin-top:6px}
.testi .nav{position:absolute;top:240px}

/* footer */
.footer{position:absolute;left:0;top:4826px;width:1200px;height:419px;background:var(--footer)}
.footer .col{position:absolute;top:0;height:337px;border-right:1px solid #d8d8d8}
.footer .logo{position:absolute;left:157px;top:92px;color:var(--green);font-size:34px}
.social{position:absolute;left:155px;top:162px;display:flex;gap:10px}
.social span{width:36px;height:36px;border:1.5px solid #333;border-radius:50%}
.footer h4{position:absolute;top:66px;font-size:21px;font-weight:700}
.links{position:absolute;left:408px;top:118px;list-style:none;font-size:12.5px;line-height:21.2px}
.contact{position:absolute;left:600px;font-size:12.5px;line-height:21px;display:flex;gap:16px;align-items:center}
.contact i{width:36px;height:36px;border-radius:50%;background:var(--green);display:flex;align-items:center;justify-content:center;flex:none}
.newsletter p{position:absolute;left:853px;top:120px;width:230px;font-size:12px;line-height:17px}
.newsletter .field{position:absolute;left:853px;top:172px;width:222px;height:40px;background:#fff;border-radius:20px;box-shadow:0 1px 4px rgba(0,0,0,.15);font-size:12px;color:#888;padding:12px 18px}
.newsletter .go{position:absolute;right:6px;top:4px;width:32px;height:32px;border-radius:50%;background:var(--green);display:flex;align-items:center;justify-content:center}
.copyright{position:absolute;left:157px;top:370px;font-size:11.5px}
.cards{position:absolute;left:824px;top:364px;display:flex;gap:8px}
.cards span{width:32px;height:20px;border-radius:3px;border:1px solid #ccc}
</style>
</head>
<body>

<header class="topbar">
  <a class="logo" href="#">Velduna.com</a>
  <div class="search">
    <span class="cat">All <svg width="8" height="6"><path d="M0 0h8L4 6z" fill="#333"/></svg></span>
    <span class="kw">Enter Keyword</span>
    <svg width="16" height="16" viewBox="0 0 16 16"><circle cx="6.5" cy="6.5" r="5" fill="none" stroke="#222" stroke-width="2"/><path d="M10.5 10.5L15 15" stroke="#222" stroke-width="2.2"/></svg>
  </div>
  <div class="acct" style="left:824px">Hello sign in<b>Accounts &amp; Lists ▾</b></div>
  <div class="acct" style="left:1018px">Returns<b>&amp; Orders ▾</b></div>
</header>

<nav class="navbar">
  <ul>
    <li style="left:96px">HOME</li>
    <li style="left:174px">OFFICE SUPPLIES</li>
    <li style="left:324px">PACKING SUPPLIES</li>
    <li style="left:485px">HOME CONSUMABLES</li>
    <li style="left:663px">TODAY'S DEAL</li>
    <li style="left:793px">CONTACT</li>
  </ul>
  <div class="cart">
    <svg width="16" height="14" viewBox="0 0 16 14"><path d="M8 14L1.5 7.5A4 4 0 0 1 8 2.5a4 4 0 0 1 6.5 5z" fill="var(--green)"/></svg>
    <span style="margin-left:14px;display:flex;gap:10px;align-items:center"><svg width="16" height="14" viewBox="0 0 16 14"><path d="M0 1h3l2 8h9l2-6H4" fill="none" stroke="var(--green)" stroke-width="2"/><circle cx="6" cy="12" r="1.6" fill="var(--green)"/><circle cx="13" cy="12" r="1.6" fill="var(--green)"/></svg>(Cart(0.00)</span>
  </div>
</nav>

<section class="hero">
  <svg class="abs" style="left:0;top:0" width="1200" height="551">
    <circle cx="1160" cy="30" r="110" fill="var(--green)"/>
    <circle cx="70" cy="620" r="210" fill="var(--green)"/>
  </svg>
  <h1>Office Supplies, packing Supplies &amp; Home Consumables</h1>
  <div class="sale">SALE UPTO 40% OFF</div>
  <a class="btn" href="#">SHOP NOW</a>
  <div class="art" role="img" aria-label="Black office desk with a laptop, desk lamp and potted flowers"></div>
</section>

<div class="notice">You are on Velduna.com. You can also shop on velduna for office,packing supplies &amp; home consumables with fast delivery. <a href="#">Click here to go to Velduna.com</a></div>

<section class="catcard" style="left:96px">
  <h3>Office Supplies</h3>
  <div class="grid">
    <div class="item"><span class="ph" role="img" aria-label="Wooden table" style="background:#c08a5a"></span><span class="label">Table</span></div>
    <div class="item"><span class="ph" role="img" aria-label="Office chair" style="background:#3a3a3a"></span><span class="label">Chairs</span></div>
    <div class="item"><span class="ph" role="img" aria-label="Desk lamp" style="background:#444"></span><span class="label">Lamps</span></div>
    <div class="item"><span class="ph" role="img" aria-label="Office desk" style="background:#5a4a42"></span><span class="label">Office Desk</span></div>
  </div>
  <a class="outline-btn" href="#">SHOP NOW</a>
</section>
<section class="catcard" style="left:355px">
  <h3>Packing Supplies</h3>
  <div class="grid">
    <div class="item"><span class="ph" role="img" aria-label="Stack of cardboard boxes" style="background:#c69a68"></span><span class="label">Boxes</span></div>
    <div class="item"><span class="ph" role="img" aria-label="Roll of packing tape" style="background:#d9c4a8"></span><span class="label">Tape</span></div>
    <div class="item"><span class="ph" role="img" aria-label="Plastic covers" style="background:#3f5f8a"></span><span class="label">Covers</span></div>
    <div class="item"><span class="ph" role="img" aria-label="Colourful rubber bands" style="background:#d98a3a"></span><span class="label">Rubbers</span></div>
  </div>
  <a class="outline-btn" href="#">SHOP NOW</a>
</section>
<section class="catcard" style="left:612px">
  <h3>Home Consumables</h3>
  <div class="grid">
    <div class="item"><span class="ph" role="img" aria-label="Kitchen sponge" style="background:#7fc3c9"></span><span class="label">Sponge</span></div>
    <div class="item"><span class="ph" role="img" aria-label="Dish soap bottle" style="background:#e8c534"></span><span class="label">Dish Soap</span></div>
    <div class="item"><span class="ph" role="img" aria-label="Detergent bottle" style="background:#b9d6e6"></span><span class="label">Detergent</span></div>
    <div class="item"><span class="ph" role="img" aria-label="Toilet paper rolls" style="background:#e6e6e6"></span><span class="label">Toilet Papers</span></div>
  </div>
  <a class="outline-btn" href="#">SHOP NOW</a>
</section>

<aside class="signin">
  <h3>Sign in for the best experience</h3>
  <a class="outline-btn" href="#">SIGN IN SECURELY</a>
</aside>
<aside class="ship">We ship our products<br>the world wide
  <span class="ph" role="img" aria-label="Cardboard shipping boxes"></span>
</aside>

<section class="panel" style="top:1206px;height:453px">
  <h2 style="top:40px">Top Sellers</h2>
  <div class="card" style="left:16px;top:106px;height:296px"><span class="ph" role="img" aria-label="Office table with chair and lamp" style="background:#6b5a4e"></span><div class="name">Office Table</div><div class="price">$150.00</div></div>
  <div class="card" style="left:265px;top:106px;height:296px"><span class="ph" role="img" aria-label="Packing supplies: box, tape and tubes" style="background:#b58b5a"></span><div class="name">Packing Supplies</div><div class="price">$120.00</div></div>
  <div class="card" style="left:516px;top:106px;height:296px"><span class="ph" role="img" aria-label="Laundry detergent bottles" style="background:#5fa0d6"></span><div class="name">Laundry Detergent</div><div class="price">$110.00</div></div>
  <div class="card" style="left:771px;top:106px;height:296px"><span class="ph" role="img" aria-label="Black leather office chair" style="background:#2e2e2e"></span><div class="name">Office Chair</div><div class="price">$1,110.00</div></div>
  <span class="arrow l" style="left:0;top:222px"><svg width="10" height="16"><path d="M8 2L2 8l6 6" fill="none" stroke="#fff" stroke-width="2"/></svg></span>
  <span class="arrow r" style="left:982px;top:222px"><svg width="10" height="16"><path d="M2 2l6 6-6 6" fill="none" stroke="#fff" stroke-width="2"/></svg></span>
</section>

<section class="panel" style="top:1706px;height:461px">
  <h2 style="top:36px">Frequently Purchased Office Supplies</h2>
  <div class="card" style="left:16px;top:108px;height:296px"><span class="ph" role="img" aria-label="Black desk telephone" style="background:#2f2f2f"></span><div class="name">Land Lane Phone</div><div class="price">$1150.00</div></div>
  <div class="card" style="left:265px;top:108px;height:296px"><span class="ph" role="img" aria-label="Office desk with red chair" style="background:#5a4d49"></span><div class="name">Office Table</div><div class="price">$1250.00</div></div>
  <div class="card" style="left:516px;top:108px;height:296px"><span class="ph" role="img" aria-label="Office desk lamp" style="background:#6a5440"></span><div class="name">Office Lamp</div><div class="price">$250.00</div></div>
  <div class="card" style="left:771px;top:108px;height:296px"><span class="ph" role="img" aria-label="Black office chair" style="background:#2a2a2a"></span><div class="name">Office Chair</div><div class="price">$2250.00</div></div>
  <span class="arrow l" style="left:0;top:227px"><svg width="10" height="16"><path d="M8 2L2 8l6 6" fill="none" stroke="#fff" stroke-width="2"/></svg></span>
  <span class="arrow r" style="left:982px;top:227px"><svg width="10" height="16"><path d="M2 2l6 6-6 6" fill="none" stroke="#fff" stroke-width="2"/></svg></span>
</section>

<article class="feature" style="left:96px"><h2>Style Your Office</h2><span class="ph" role="img" aria-label="Modern office interior with dark walls and meeting table" style="background:linear-gradient(180deg,#3b5560,#24343b)"></span><a href="#">SHOP NOW</a></article>
<article class="feature" style="left:439px"><h2>Start Packing</h2><span class="ph" role="img" aria-label="Hands taping a cardboard box with a tape dispenser" style="background:linear-gradient(180deg,#b79a72,#8a6a3f)"></span><a href="#">SEE MORE</a></article>
<article class="feature" style="left:784px"><h2>Decor Your Home</h2><span class="ph" role="img" aria-label="Laundry room with folded towels on a washing machine" style="background:linear-gradient(180deg,#e8e6e2,#cfccc6)"></span><a href="#">SHOP NOW</a></article>

<section class="panel" style="top:2708px;height:526px">
  <h2 style="top:40px">Popular Packing Supplies <a href="#">SHOP NOW</a></h2>
  <div class="card" style="left:16px;top:112px;height:355px"><span class="ph" role="img" aria-label="Rolls of clear packing tape" style="background:#d8ccb6"></span><div class="name">Tape</div><div class="price">$60.00</div><a class="outline-btn" href="#">SHOP NOW</a></div>
  <div class="card" style="left:265px;top:112px;height:355px"><span class="ph" role="img" aria-label="Open cardboard packing box" style="background:#c49866"></span><div class="name">Packing Boxes</div><div class="price">$350.00</div><a class="outline-btn" href="#">SHOP NOW</a></div>
  <div class="card" style="left:516px;top:112px;height:355px"><span class="ph" role="img" aria-label="Rolls of stretch wrap sheets" style="background:#e2dcd8"></span><div class="name">Packing Sheets</div><div class="price">$150.00</div><a class="outline-btn" href="#">SHOP NOW</a></div>
  <div class="card" style="left:771px;top:112px;height:355px"><span class="ph" role="img" aria-label="Tape gun dispenser" style="background:#3a64a8"></span><div class="name">Packing Supplies</div><div class="price">$150.00</div><a class="outline-btn" href="#">SHOP NOW</a></div>
  <span class="arrow l" style="left:0;top:240px"><svg width="10" height="16"><path d="M8 2L2 8l6 6" fill="none" stroke="#fff" stroke-width="2"/></svg></span>
  <span class="arrow r" style="left:982px;top:240px"><svg width="10" height="16"><path d="M2 2l6 6-6 6" fill="none" stroke="#fff" stroke-width="2"/></svg></span>
</section>

<section class="panel" style="top:3285px;height:535px">
  <h2 style="top:55px">Trendind Home Consumables <a href="#">SHOP NOW</a></h2>
  <div class="card" style="left:16px;top:123px;height:353px"><span class="ph" role="img" aria-label="Washing detergent bottle with flowers" style="background:#cfe4ea"></span><div class="name">Washing Detergent</div><div class="price">$160.00</div><a class="outline-btn" href="#">SHOP NOW</a></div>
  <div class="card" style="left:265px;top:123px;height:353px"><span class="ph" role="img" aria-label="Toilet paper roll" style="background:#ececec"></span><div class="name">Toilet Papers</div><div class="price">$160.00</div><a class="outline-btn" href="#">SHOP NOW</a></div>
  <div class="card" style="left:516px;top:123px;height:353px"><span class="ph" role="img" aria-label="Green folded napkins" style="background:#2f7a55"></span><div class="name">Toilet Napkins</div><div class="price">$180.00</div><a class="outline-btn" href="#">SHOP NOW</a></div>
  <div class="card" style="left:771px;top:123px;height:353px"><span class="ph" role="img" aria-label="Dish soap and sponge" style="background:#2d6fd1"></span><div class="name">Sponge</div><div class="price">$60.00</div><a class="outline-btn" href="#">SHOP NOW</a></div>
  <span class="arrow l" style="left:0;top:235px"><svg width="10" height="16"><path d="M8 2L2 8l6 6" fill="none" stroke="#fff" stroke-width="2"/></svg></span>
  <span class="arrow r" style="left:982px;top:235px"><svg width="10" height="16"><path d="M2 2l6 6-6 6" fill="none" stroke="#fff" stroke-width="2"/></svg></span>
</section>

<section class="mission">
  <h2>Our Mission</h2>
  <p>Lorem ipsum dolor sit amet, consectetur adipiscing elit, sed do eiusmod tempor incididunt ut labore et dolore magna aliqua. Ut enim ad minim veniam, quis nostrud exercitation ullamco laboris nisi ut aliquip ex ea commodo consequat. Duis aute irure dolor in reprehenderit in voluptate velit esse cillum dolore eu fugiat nulla pariatur. Excepteur sint occaecat cupidatat non proident, sunt in culpa qui officia deserunt mollit anim id est laborum.Sed ut doloremque laudantium, totam rem aperiam, eaque ipsa quae ab illo inventore veritatis et quasi architecto beatae vitae dicta sunt explicabo.</p>
  <a class="btn" href="#">LEARN MORE</a>
  <span class="ph" role="img" aria-label="Open office with rows of desks" style="left:636px;top:3932px;width:272px;height:163px;background:linear-gradient(180deg,#5a6670,#2f3a40)"></span>
  <span class="ph" role="img" aria-label="Cardboard boxes with tape and cutter" style="left:903px;top:3899px;width:210px;height:186px;background:linear-gradient(180deg,#dcd4c6,#b28e60)"></span>
  <span class="ph" role="img" aria-label="Towels and detergent bottle" style="left:544px;top:4089px;width:271px;height:183px;background:linear-gradient(180deg,#b7d6a8,#7fc3c4)"></span>
  <span class="ph" role="img" aria-label="Office room with wooden floor" style="left:809px;top:4079px;width:294px;height:169px;background:linear-gradient(180deg,#3a3a3a,#8a6a4c)"></span>
</section>

<section class="testi">
  <h2>TESTIMONIALS</h2>
  <div class="quote">”</div>
  <p>Sed ut perspiciatis unde omnis iste natus error sit voluptatem accusantium doloremque laudantium, totam rem aperiam, eaque ipsa quae ab illo inventore veritatis et quasi archi-tecto beatae vitae dicta sunt explicabo enim ipsam voluptatem quia volup</p>
  <span class="avatar" role="img" aria-label="Customer portrait"></span>
  <div class="who">Mara Ellison
    <div class="stars">
      <svg width="14" height="14" viewBox="0 0 10 10"><path d="M5 0l1.5 3.3 3.5.4-2.6 2.4.7 3.5L5 7.8 1.9 9.6l.7-3.5L0 3.7l3.5-.4z" fill="#f5c518"/></svg>
      <svg width="14" height="14" viewBox="0 0 10 10"><path d="M5 0l1.5 3.3 3.5.4-2.6 2.4.7 3.5L5 7.8 1.9 9.6l.7-3.5L0 3.7l3.5-.4z" fill="#f5c518"/></svg>
      <svg width="14" height="14" viewBox="0 0 10 10"><path d="M5 0l1.5 3.3 3.5.4-2.6 2.4.7 3.5L5 7.8 1.9 9.6l.7-3.5L0 3.7l3.5-.4z" fill="#f5c518"/></svg>
      <svg width="14" height="14" viewBox="0 0 10 10"><path d="M5 0l1.5 3.3 3.5.4-2.6 2.4.7 3.5L5 7.8 1.9 9.6l.7-3.5L0 3.7l3.5-.4z" fill="#f5c518"/></svg>
      <svg width="14" height="14" viewBox="0 0 10 10"><path d="M5 0l1.5 3.3 3.5.4-2.6 2.4.7 3.5L5 7.8 1.9 9.6l.7-3.5L0 3.7l3.5-.4z" fill="#f5c518"/></svg>
    </div>
  </div>
  <svg class="nav" style="left:136px" width="22" height="40"><path d="M19 2L3 20l16 18" fill="none" stroke="#fff" stroke-width="3"/></svg>
  <svg class="nav" style="left:1048px" width="22" height="40"><path d="M3 2l16 18L3 38" fill="none" stroke="#fff" stroke-width="3"/></svg>
</section>

<footer class="footer">
  <div class="col" style="left:0;width:367px"></div>
  <div class="col" style="left:367px;width:184px"></div>
  <div class="col" style="left:551px;width:261px"></div>
  <span class="logo">Velduna.com</span>
  <div class="social"><span></span><span></span><span></span><span></span></div>

  <h4 style="left:408px">Links</h4>
  <ul class="links"><li>Home</li><li>About</li><li>Shop</li><li>Products</li><li>My Account</li><li>Shipping &amp; Delivery</li><li>FAQ's</li></ul>

  <h4 style="left:590px">Contact Us</h4>
  <div class="contact" style="top:118px">
    <i><svg width="14" height="18" viewBox="0 0 14 18"><path d="M7 0a7 7 0 0 1 7 7c0 5-7 11-7 11S0 12 0 7a7 7 0 0 1 7-7z" fill="#fff"/><circle cx="7" cy="7" r="2.5" fill="var(--green)"/></svg></i>
    <span>Location Name<br>Dummy address line<br>Ashvale 4120 RD (1180)</span>
  </div>
  <div class="contact" style="top:187px">
    <i><svg width="16" height="16" viewBox="0 0 16 16"><path d="M3 1l3 3-2 2a10 10 0 0 0 6 6l2-2 3 3-2 2C7 15 1 9 1 3z" fill="#fff"/></svg></i>
    <span>Phone:555.210.0147</span>
  </div>
  <div class="contact" style="top:238px">
    <i><svg width="16" height="12" viewBox="0 0 16 12"><rect width="16" height="12" rx="1.5" fill="#fff"/><path d="M1 1l7 6 7-6" fill="none" stroke="var(--green)" stroke-width="1.5"/></svg></i>
    <span>Email info@company.com</span>
  </div>

  <div class="newsletter">
    <h4 style="left:853px">Newsletter Sign up</h4>
    <p>Lorem ipsum dolor sit amet, conse ctetur adipiscing elit sed.</p>
    <div class="field">Email
      <span class="go"><svg width="14" height="12" viewBox="0 0 14 12"><path d="M0 6h12M7 1l5 5-5 5" fill="none" stroke="#fff" stroke-width="2"/></svg></span>
    </div>
  </div>

  <div class="copyright">© 2022 All Rights Reserved.Terms &amp; Conditions Privacy Policy</div>
  <div class="cards">
    <span style="background:#2c3e7a"></span><span style="background:#fff"></span><span style="background:#222"></span><span style="background:#fff"></span><span style="background:#2a8ad6"></span><span style="background:#f1f1f1"></span><span style="background:#f2c23c"></span>
  </div>
</footer>

</body>
</html>
```